12 Meter Banner-Design Lagerhalle
Zielgruppe
Wir errichten neue Elektroanlagen für Einfamilenhäuser und Wohnungen.
Hallo,
wir möchten auf 12 Meter drei Banner spannen um die unschönen Rohre und Kabel zu verdecken. Jeder der drei Banner soll 400cm breit und 160cm hoch werden.
-Banner 1 links: Motivationsspruch groß, mittig - : Wer immer tut, was er schon kann, bleibt immer das, was er schon ist.
- Banner 2 mitte : Komfortzone ( Grafiken habe ich im Anhang von dem Aufbau der Komfortzone ) Toll wäre ein selbst erstelltes Design passend zum Unternehmen / Farben Schriftart etc.
-Banner 3 rechts: Motivationsspruch : Zusammenkommen ist ein Beginn, zusammenbleiben ist ein Fortschritt, zusammenarbeiten ist ein Erfolg.
- Design nach Vorgabe Druckpilot ( Datasheet) erstellen
Gundsätzlich wäre super, wenn alle 3 Designs/ Banner miteinander harmonieren. Alles andere ist der Kreativität überlassen.
Schriftart: Fira Sans / Montserrat
Wir würden uns über eine Zusammenarbeit freuen.
Beste Grüße

```html
<!DOCTYPE html>
<html lang="de">
<head>
<meta charset="utf-8">
<title>Banner-Serie Lagerhalle – Volta Elektro</title>
<link rel="stylesheet" href="https://fonts.googleapis.com/css2?family=Fira+Sans+Condensed:wght@400;500&family=Orbitron:wght@500;600&display=swap">
<style>
  :root {
    --stage: #575757;
    --brand: #1a96cd;
    --brand-dark: #0f5a7c;
    --paper: #ffffff;
    --ink: #1b1b1b;
    --eyelet: #b9bcbf;
    --frame: #cfd3d6;
  }
  * { box-sizing: border-box; margin: 0; padding: 0; }
  html, body { width: 1200px; height: 1200px; overflow: hidden; }
  body { background: var(--stage); position: relative; font-family: "Fira Sans Condensed", sans-serif; }

  .banner {
    position: absolute;
    width: 1133px; height: 452px;
    overflow: hidden;
  }
  .banner--small { transform: scale(0.332); transform-origin: 0 0; }
  .banner--blue { background: var(--brand); color: var(--paper); }
  .banner--white { background: var(--paper); color: var(--ink); }

  .banner__frame {
    position: absolute; inset: 14px;
    border: 1px solid var(--frame);
  }
  .banner--blue .banner__frame { border-color: rgba(255,255,255,0.25); }

  .eyelets { position: absolute; }
  .eyelets--top, .eyelets--bottom {
    left: 3px; right: 3px; height: 14px;
    background: radial-gradient(circle at 50% 50%, transparent 2.5px, var(--eyelet) 3px, var(--eyelet) 5px, transparent 5.5px) 0 0 / 139.4px 14px repeat-x;
    background-position: -63px 0;
  }
  .eyelets--top { top: 2px; }
  .eyelets--bottom { bottom: 2px; }
  .eyelets--left, .eyelets--right {
    top: 2px; bottom: 2px; width: 14px;
    background: radial-gradient(circle at 50% 50%, transparent 2.5px, var(--eyelet) 3px, var(--eyelet) 5px, transparent 5.5px) 0 0 / 14px 145px repeat-y;
    background-position: 0 -65px;
  }
  .eyelets--left { left: 2px; }
  .eyelets--right { right: 2px; }

  /* Motivation quote banners */
  .quote {
    position: absolute;
    font-family: "Orbitron", sans-serif;
    font-weight: 500;
    text-align: center;
    white-space: nowrap;
  }
  .quote__line { display: block; }

  .quote--left { left: 400px; width: 780px; top: 72px; font-size: 36px; line-height: 81px; }
  .quote--team { left: 0; right: 0; top: 112px; font-size: 40px; line-height: 80px; }

  .brand-mark {
    position: absolute;
    display: flex; align-items: center; gap: 14px;
    font-family: "Orbitron", sans-serif; font-weight: 600;
    color: var(--paper);
  }
  .brand-mark__dot { border: 6px solid var(--paper); border-radius: 50%; }
  .brand-mark--left { left: 40px; top: 190px; font-size: 34px; }
  .brand-mark--left .brand-mark__dot { width: 56px; height: 56px; }
  .brand-mark--corner { right: 40px; top: 40px; font-size: 28px; }
  .brand-mark--corner .brand-mark__dot { width: 48px; height: 48px; }

  /* Comfort zone banner */
  .zone {
    position: absolute; top: 37px;
    width: 227px; margin-left: -113.5px;
    text-align: center;
  }
  .zone__badge {
    position: relative; width: 224px; height: 224px; margin: 0 auto;
  }
  .zone__circle {
    position: absolute; inset: 0; border-radius: 50%; background: var(--brand);
  }
  .zone__label {
    position: absolute; left: -1.5px; width: 227px; top: 163px; height: 36px;
    background: var(--brand-dark); color: var(--paper);
    font-weight: 500; font-size: 24px; line-height: 36px; letter-spacing: 0.5px;
  }
  .zone__traits { list-style: none; margin-top: 24px; font-size: 21px; line-height: 35px; color: var(--ink); }
</style>
</head>
<body>

<!-- Left banner: quote -->
<section class="banner banner--blue banner--small" style="left:30px; top:47px;">
  <div class="banner__frame"></div>
  <div class="eyelets eyelets--top"></div><div class="eyelets eyelets--bottom"></div>
  <div class="eyelets eyelets--left"></div><div class="eyelets eyelets--right"></div>
  <div class="brand-mark brand-mark--left"><span class="brand-mark__dot"></span>Volta Elektro</div>
  <p class="quote quote--left">
    <span class="quote__line">Wer immer tut,</span>
    <span class="quote__line">was er schon kann,</span>
    <span class="quote__line">bleibt immer das,</span>
    <span class="quote__line">was er schon ist.</span>
  </p>
</section>

<!-- Middle banner: zones (small preview) -->
<section class="banner banner--white banner--small" style="left:411px; top:47px;">
  <div class="banner__frame"></div>
  <div class="eyelets eyelets--top"></div><div class="eyelets eyelets--bottom"></div>
  <div class="eyelets eyelets--left"></div><div class="eyelets eyelets--right"></div>
  <div class="zone" style="left:143px">
    <div class="zone__badge"><div class="zone__circle" role="img" aria-label="Illustration eines Sofas"></div><div class="zone__label">KOMFORTZONE</div></div>
    <ul class="zone__traits"><li>Kontrolle</li><li>Gewohnheit</li><li>Sicherheit</li><li>Routine</li></ul>
  </div>
  <div class="zone" style="left:424px">
    <div class="zone__badge"><div class="zone__circle" role="img" aria-label="Illustration eines Hasen, der aus einem Loch schaut"></div><div class="zone__label">ANGSTZONE</div></div>
    <ul class="zone__traits"><li>Unsicherheit</li><li>Ablehnung</li><li>Ausreden</li><li>Abbruch</li></ul>
  </div>
  <div class="zone" style="left:705px">
    <div class="zone__badge"><div class="zone__circle" role="img" aria-label="Illustration eines Teleskops"></div><div class="zone__label">LERNZONE</div></div>
    <ul class="zone__traits"><li>neue Skills</li><li>Erfahrungen</li><li>Selbstvertrauen</li><li>Zonenausbau</li></ul>
  </div>
  <div class="zone" style="left:987px">
    <div class="zone__badge"><div class="zone__circle" role="img" aria-label="Illustration eines Astronauten auf einer Rakete"></div><div class="zone__label">WACHSTUMSZONE</div></div>
    <ul class="zone__traits"><li>Zielerreichung</li><li>Sinnfindung</li><li>Selbstsicherheit</li><li>Zufriedenheit</li></ul>
  </div>
</section>

<!-- Right banner: team quote (small preview) -->
<section class="banner banner--blue banner--small" style="left:793px; top:47px;">
  <div class="banner__frame"></div>
  <div class="eyelets eyelets--top"></div><div class="eyelets eyelets--bottom"></div>
  <div class="eyelets eyelets--left"></div><div class="eyelets eyelets--right"></div>
  <div class="brand-mark brand-mark--corner"><span class="brand-mark__dot"></span>Volta Elektro</div>
  <p class="quote quote--team">
    <span class="quote__line">Zusammen ist ein Beginn,</span>
    <span class="quote__line">zusammenbleiben ist ein Fortschritt,</span>
    <span class="quote__line">zusammenarbeiten ist ein Erfolg</span>
  </p>
</section>

<!-- Middle banner: zones (detail) -->
<section class="banner banner--white" style="left:34px; top:255px;">
  <div class="banner__frame"></div>
  <div class="eyelets eyelets--top"></div><div class="eyelets eyelets--bottom"></div>
  <div class="eyelets eyelets--left"></div><div class="eyelets eyelets--right"></div>
  <div class="zone" style="left:143px">
    <div class="zone__badge"><div class="zone__circle" role="img" aria-label="Illustration eines Sofas"></div><div class="zone__label">KOMFORTZONE</div></div>
    <ul class="zone__traits"><li>Kontrolle</li><li>Gewohnheit</li><li>Sicherheit</li><li>Routine</li></ul>
  </div>
  <div class="zone" style="left:424px">
    <div class="zone__badge"><div class="zone__circle" role="img" aria-label="Illustration eines Hasen, der aus einem Loch schaut"></div><div class="zone__label">ANGSTZONE</div></div>
    <ul class="zone__traits"><li>Unsicherheit</li><li>Ablehnung</li><li>Ausreden</li><li>Abbruch</li></ul>
  </div>
  <div class="zone" style="left:705px">
    <div class="zone__badge"><div class="zone__circle" role="img" aria-label="Illustration eines Teleskops"></div><div class="zone__label">LERNZONE</div></div>
    <ul class="zone__traits"><li>neue Skills</li><li>Erfahrungen</li><li>Selbstvertrauen</li><li>Zonenausbau</li></ul>
  </div>
  <div class="zone" style="left:987px">
    <div class="zone__badge"><div class="zone__circle" role="img" aria-label="Illustration eines Astronauten auf einer Rakete"></div><div class="zone__label">WACHSTUMSZONE</div></div>
    <ul class="zone__traits"><li>Zielerreichung</li><li>Sinnfindung</li><li>Selbstsicherheit</li><li>Zufriedenheit</li></ul>
  </div>
</section>

<!-- Right banner: team quote (detail) -->
<section class="banner banner--blue" style="left:34px; top:731px;">
  <div class="banner__frame"></div>
  <div class="eyelets eyelets--top"></div><div class="eyelets eyelets--bottom"></div>
  <div class="eyelets eyelets--left"></div><div class="eyelets eyelets--right"></div>
  <div class="brand-mark brand-mark--corner"><span class="brand-mark__dot"></span>Volta Elektro</div>
  <p class="quote quote--team">
    <span class="quote__line">Zusammen ist ein Beginn,</span>
    <span class="quote__line">zusammenbleiben ist ein Fortschritt,</span>
    <span class="quote__line">zusammenarbeiten ist ein Erfolg</span>
  </p>
</section>

</body>
</html>
```